Larkspur Ridge Management - Business Cards

I need business cards. My current logo was designed by a designer at this site and I very much like and am happy with the results. I would like a business card that is trendy, unique, current yet professional. I deal with high net worth clients daily

Target Market(s)

Out of state investors looking to get into the rental market in Ohio

Industry/Entity Type

Property Management, Consulting

Contact Information for Business Card

Name, Title (Chief Financial Officer) office phone number (555) 817-3094 website address larkridgemgmt.example

Font styles to use
Sans Serif

Colors
0054AA
0677BA
7BADD7
CADEEF
E8F1F8
0094D4
00A9DD
6FCCEA
C7EBF8
E9F6FB
00AB8E
00BBA5
67D7C9
C6EFE9
E9F9F6

```html
<!DOCTYPE html>
<html lang="en">
<head>
<meta charset="utf-8">
<title>Larkspur Ridge Management – Business Cards</title>
<link rel="stylesheet" href="https://fonts.googleapis.com/css2?family=Open+Sans:ital,wght@0,400;0,600;0,700;0,800;1,400&display=swap">
<style>
  :root {
    --navy: #1f2b4e;
    --red: #c1232b;
    --red-deep: #8f111b;
    --white: #ffffff;
    --grey: #555555;
    --backdrop: #161616;
  }
  * { box-sizing: border-box; margin: 0; padding: 0; }
  html, body { width: 1200px; height: 963px; overflow: hidden; }
  body {
    background: var(--backdrop);
    font-family: "Open Sans", Arial, sans-serif;
    position: relative;
  }
  .card {
    position: absolute;
    width: 540px;
    height: 309px;
    border-radius: 22px;
    overflow: hidden;
    background: var(--white);
  }
  /* Front */
  .card-front { left: 40px; top: 327px; }
  .front-brand {
    position: absolute;
    top: 62px; left: 0; right: 0;
    text-align: center;
    color: var(--navy);
    font-weight: 800;
    font-size: 25px;
    line-height: 1.2;
    letter-spacing: 1px;
    text-transform: uppercase;
  }
  .front-person {
    position: absolute;
    left: 150px; top: 168px;
  }
  .person-name {
    color: var(--red);
    font-weight: 800;
    font-size: 21px;
    letter-spacing: 0.5px;
    text-transform: uppercase;
  }
  .person-title {
    color: var(--grey);
    font-size: 16px;
    margin-top: -2px;
  }
  .front-band {
    position: absolute;
    left: 0; right: 0; bottom: 0;
    height: 58px;
    background: var(--navy);
    border-top: 4px solid var(--white);
    box-shadow: 0 -3px 0 var(--red);
    display: flex;
    align-items: center;
    justify-content: center;
    gap: 28px;
    color: var(--white);
    font-size: 16px;
  }
  .contact-item { display: flex; align-items: center; gap: 8px; }
  .contact-item svg { width: 16px; height: 16px; }

  /* Back */
  .card-back { left: 620px; top: 327px; background: var(--navy); }
  .back-top {
    position: absolute;
    left: 0; right: 0; top: 0;
    height: 70px;
    background: linear-gradient(100deg, var(--red-deep), var(--red));
  }
  .back-stripe {
    position: absolute;
    left: 0; right: 0; top: 76px;
    height: 6px;
    background: var(--white);
  }
  .back-panel {
    position: absolute;
    left: 60px; right: 60px; top: 112px; bottom: 0;
    background: var(--white);
    border-top: 8px solid var(--red);
    display: flex;
    align-items: center;
    justify-content: center;
    text-align: center;
  }
  .back-brand {
    color: var(--navy);
    font-weight: 800;
    font-size: 24px;
    line-height: 1.25;
    letter-spacing: 1px;
    text-transform: uppercase;
  }
</style>
</head>
<body>
  <section class="card card-front" aria-label="Business card front">
    <div class="front-brand">Larkspur Ridge<br>Management</div>
    <div class="front-person">
      <div class="person-name">Daniel Reyes</div>
      <div class="person-title">Chief Financial Officer</div>
    </div>
    <div class="front-band">
      <span class="contact-item">
        <svg viewBox="0 0 24 24" aria-hidden="true"><path fill="#c1232b" d="M6.6 10.8a15.1 15.1 0 0 0 6.6 6.6l2.2-2.2c.3-.3.7-.4 1-.2 1.1.4 2.3.6 3.6.6.6 0 1 .4 1 1V20c0 .6-.4 1-1 1A17 17 0 0 1 3 4c0-.6.4-1 1-1h3.5c.6 0 1 .4 1 1 0 1.3.2 2.5.6 3.6.1.3 0 .7-.2 1z"/></svg>
        (555) 817-3094
      </span>
      <span class="contact-item">
        <svg viewBox="0 0 24 24" aria-hidden="true"><circle cx="12" cy="12" r="10" fill="#c1232b"/><path d="M2 12h20M12 2c3 3 3 17 0 20M12 2c-3 3-3 17 0 20" stroke="#1f2b4e" stroke-width="1.5" fill="none"/></svg>
        www.larkridgemgmt.example
      </span>
    </div>
  </section>

  <section class="card card-back" aria-label="Business card back">
    <div class="back-top"></div>
    <div class="back-stripe"></div>
    <div class="back-panel">
      <div class="back-brand">Larkspur Ridge<br>Management</div>
    </div>
  </section>
</body>
</html>
```